Broschüre für Toben – Balgen – Kraftprobe
Zielgruppe
Wir bieten Rangel und Raufkurse für Kinder ab dem Vorschulalter bis zu weiterführenden Schulen. Die Broschüre erhalten Lehrer, Erzieher und Direktoren der Einrichtungen an denen die Kurse Angeboten werden.
Aufgabenstellung
Design sollte eher Schlicht und modern wirken und an der homepage
www.boden-lernwerk.de orientiert sein.
Infobroschüre zum Durchblättern, kein Folder. Seitenfolge wie auf der Powerpoint präsentation.

```html
<!DOCTYPE html>
<html lang="de">
<head>
<meta charset="utf-8">
<title>Toben – Balgen – Kraftprobe · Broschüre Seite 6–7</title>
<link href="https://fonts.googleapis.com/css2?family=Open+Sans:wght@400;600;700;800&display=swap" rel="stylesheet">
<style>
  :root {
    --bg: #d9d9d9;
    --paper: #ffffff;
    --ink: #3a3a3a;
    --ink-soft: #555555;
    --red: #9b1b1e;
    --red-box: #a01a1c;
    --rule: #9a9a9a;
  }
  * { box-sizing: border-box; margin: 0; padding: 0; }
  html, body { width: 1200px; height: 833px; overflow: hidden; }
  body {
    background: var(--bg);
    font-family: "Open Sans", Arial, sans-serif;
    color: var(--ink);
  }
  .spread {
    position: absolute;
    left: 50px; top: 27px;
    width: 1100px; height: 778px;
    display: flex;
    box-shadow: 0 6px 22px rgba(0,0,0,.18);
  }
  .page {
    position: relative;
    width: 550px; height: 778px;
    background: var(--paper);
    padding: 46px 40px 0;
    font-size: 8.4px;
    line-height: 1.5;
  }
  .page--left { background: linear-gradient(to left, #ececec 0, var(--paper) 22px); }
  .page--right { background: linear-gradient(to right, #ececec 0, var(--paper) 22px); }

  .title {
    color: var(--red);
    font-weight: 700;
    font-size: 29px;
    letter-spacing: .5px;
    line-height: 1.2;
  }
  .title-rule {
    width: 40px; height: 2px;
    background: var(--red);
    margin: 12px 0 14px;
  }
  .intro {
    font-weight: 700;
    font-size: 12.6px;
    line-height: 1.45;
    color: #2e2e2e;
    max-width: 460px;
  }
  .photo {
    width: 470px; height: 190px;
    margin: 16px 0 18px;
    background: linear-gradient(100deg, #d9b48c 0%, #e9e2d6 22%, #7fae4a 45%, #5f9236 65%, #8a8a84 85%, #b7b4ae 100%);
  }
  .columns {
    display: grid;
    grid-template-columns: 1fr 1fr;
    column-gap: 22px;
  }
  .lead { display: flow-root; margin-bottom: 10px; }
  .dropcap {
    float: left;
    font-size: 54px;
    font-weight: 800;
    line-height: .85;
    margin: 3px 8px 0 0;
    color: #3a3a3a;
  }
  .lead-text { font-weight: 700; font-size: 10px; line-height: 1.4; color: #2e2e2e; }
  p { margin-bottom: 10px; text-align: justify; hyphens: auto; }
  .phase-head { font-weight: 700; display: block; color: #2e2e2e; }

  .folio {
    position: absolute;
    bottom: 26px;
    font-size: 7.5px;
    letter-spacing: .8px;
    color: var(--ink-soft);
  }
  .page--left .folio { left: 40px; padding-left: 10px; border-left: 1px solid var(--rule); height: 34px; display: flex; align-items: flex-start; }
  .page--right .folio { right: 40px; padding-right: 10px; border-right: 1px solid var(--rule); height: 34px; display: flex; align-items: flex-start; }
  .wordmark {
    position: absolute;
    bottom: 30px;
    font-size: 9px;
    font-weight: 600;
    letter-spacing: 1.2px;
    color: var(--ink-soft);
  }
  .page--left .wordmark { right: 44px; }
  .page--right .wordmark { left: 44px; }

  .infobox {
    background: var(--red-box);
    color: #fff;
    border-radius: 8px;
    padding: 14px 14px 14px;
    margin-top: 8px;
    font-size: 8.2px;
    line-height: 1.5;
  }
  .infobox-head { font-weight: 700; margin-bottom: 6px; }
  .infobox ul { list-style: none; }
  .infobox li { display: flex; gap: 6px; margin-bottom: 2px; }
  .infobox svg { flex: 0 0 11px; margin-top: 2px; }
</style>
</head>
<body>
<main class="spread">
  <section class="page page--left">
    <h1 class="title">Toben – Balgen – Kraftprobe</h1>
    <div class="title-rule"></div>
    <p class="intro">Das zentrale Ziel des Programms ist es, den Kindern wichtige Kompetenzen zu vermitteln, die notwendig sind um friedlich und ohne Anleitungen miteinander kämpfen zu können.</p>
    <div class="photo" role="img" aria-label="Foto: zwei Kinder rangeln lachend miteinander, im Hintergrund grünes Laub"></div>
    <div class="columns">
      <div class="col">
        <div class="lead"><span class="dropcap">D</span><span class="lead-text">ies stellt eine hohe emotionale Herausforderung dar und kann nur erfolgen, wenn klare Regeln vereinbart und eingehalten werden.</span></div>
        <p>Um zu gewährleisten, dass das Training verletzungsfrei für alle teilnehmenden Kinder abläuft, teilen wir die Unterrichtsstunde in mehrere Phasen ein und nähern uns so dem freien Kämpfen Schritt für Schritt:</p>
        <p><span class="phase-head">Phase 1: Kennen lernen und Vertrauen aufbauen</span>Der Prozess zum Aufbau eines vertrauensvollen Verhältnisses benötigt viel Zeit und pädagogisches Feingefühl. Je nachdem, wie gut sich Teilnehmer bereits untereinander kennen und wie stark die Heterogenität der Gruppe ausfällt, kann das Kennenlernen im Sitzkreis stattfinden oder durch einfache Spiele eine Vertrauensbasis geschaffen werden.</p>
      </div>
      <div class="col">
        <p><span class="phase-head">Phase 2: Erarbeiten der Regeln, Aufbau von Körperkontakt und allgemeines Aufwärmen</span>Bereits zum Aufwärmen werden klare Regeln festgelegt. Dadurch soll den Teilnehmern verdeutlicht werden, wie wichtig die Einhaltung von Regeln allgemein und vor allem später beim Kämpfen ist. Wir nutzen verschiedene Spiele, um ersten Körperkontakt aufzubauen und um zu testen, inwieweit die Gruppe schon bereit für das Rangeln und Raufen ist. Bei älteren Kindern und Jugendlichen nutzen wir die Phase auch gerne um sie körperlich und geistig herauszufordern, indem sie sich das Raufen im Anschluss erst durch die Bewältigung der ein oder anderen Fitness- oder Kraftübung verdienen müssen.</p>
      </div>
    </div>
    <div class="folio">SEITE 6</div>
    <div class="wordmark">BODENLERNWERK</div>
  </section>

  <section class="page page--right">
    <div class="columns">
      <div class="col">
        <p><span class="phase-head">Phase 3: Technikteil</span>Einfache Basistechniken aus dem Brazilian Jiu-Jitsu reichen aus, um sein Gegenüber am Boden zu kontrollieren, ohne ihm dabei wehzutun. Die Kinder dürfen das Gezeigte partnerweise trainieren und ausprobieren. Dabei wird der Unterschied zwischen „Miteinander“ und friedlichem „Gegeneinander“ betont, damit ein Wir-Gefühl entsteht und die Kinder/Jugendlichen lernen zusammenzuarbeiten. Als zentrales Ziel gilt es, sich gegenseitig zu helfen und der bestmögliche Trainingspartner zu sein. Die Trainer helfen und passen dabei Korrekturen und Anleitungen je nach Eifer und Selbstständigkeit der einzelnen Paare an. Erste Erfolgserlebnisse und das wachsende Vertrauen in ihre Fähigkeiten zeigen den Kindern, zu was sie im Stande sind und steigert ihr Selbstbewusstsein.</p>
        <p><span class="phase-head">Phase 4: Rangel und Raufspiele:</span>Als Vorstufe zum freien Kämpfen dürfen die Teilnehmer nun erstmals vom „Miteinander“ ins spielerische „Gegeneinander“ übergehen. Wichtige Regeln werden nochmals wiederholt, bevor unter Anleitung verschiedene Positionen am Boden oder auch im Stand ausgekämpft werden dürfen. So entstehen erste Rangordnungen und wir bekommen ein gutes Gefühl dafür, wie gut einzelne Kinder mit Sieg und Niederlage umgehen können.</p>
        <p><span class="phase-head">Phase 5: Freies Kämpfen</span>Wenn deutlich wird, dass die Teilnehmer das Rangeln und Raufen in Phase 4 emotional gut verkraften, dürfen sie unangeleitet - also ohne Vorgabe einer Aufgabestellung oder einer konkreten Zielposition - weiterkämpfen. Das freie Kämpfen dient also als Messlatte und zeigt, inwieweit die pädagogisch intendierten Zielsetzungen erreicht wurden.</p>
      </div>
      <div class="col">
        <p><span class="phase-head">Phase 6: Auflockerung und Verarbeitung des Erlebten durch Meditationsphase oder Abschlussspiel</span>Ein Abschlussspiel ohne kämpferische Aspekte soll die Stunde vom Gegeneinander wieder zum Miteinander zurückführen und ein spaßiges Ende für alle gewährleisten.</p>
        <aside class="infobox">
          <p class="infobox-head">Trainingspartner, die friedlich kämpfen können, haben wichtige Kompetenzen und Werte erfolgreich verinnerlicht:</p>
          <ul>
            <li><svg width="11" height="8" viewBox="0 0 11 8"><polygon points="5.5,0 11,2.5 5.5,5 0,2.5" fill="#fff"/><path d="M2.5 3.8v2.2c1.8 1.3 4.2 1.3 6 0V3.8" fill="#fff"/></svg><span>Überlegene Kinder entwickeln eine kampfspezifische Fürsorge und achten auf die Gesundheit ihres Partners</span></li>
            <li><svg width="11" height="8" viewBox="0 0 11 8"><polygon points="5.5,0 11,2.5 5.5,5 0,2.5" fill="#fff"/><path d="M2.5 3.8v2.2c1.8 1.3 4.2 1.3 6 0V3.8" fill="#fff"/></svg><span>Unterlegene Kinder lernen sich strategisch aus misslichen Lagen zu befreien. Damit dies funktioniert müssen sie dazu in der Lage sein in Stresssituationen ruhig zu bleiben</span></li>
            <li><svg width="11" height="8" viewBox="0 0 11 8"><polygon points="5.5,0 11,2.5 5.5,5 0,2.5" fill="#fff"/><path d="M2.5 3.8v2.2c1.8 1.3 4.2 1.3 6 0V3.8" fill="#fff"/></svg><span>Die Kinder erfahren unmittelbar, dass kritische Situationen und Konflikte durch ruhig durchdachte Strategien gelöst werden können und vor allem, dass affektives oder aggressives Verhalten keinesfalls die beste Lösung darstellt</span></li>
            <li><svg width="11" height="8" viewBox="0 0 11 8"><polygon points="5.5,0 11,2.5 5.5,5 0,2.5" fill="#fff"/><path d="M2.5 3.8v2.2c1.8 1.3 4.2 1.3 6 0V3.8" fill="#fff"/></svg><span>Wenn Regeln vereinbart werden, müssen sie eingehalten werden. Die Kinder lernen, dass man respektvoll behandelt wird, wenn man anderen im Gegenzug auch respektvoll gegenübertritt</span></li>
            <li><svg width="11" height="8" viewBox="0 0 11 8"><polygon points="5.5,0 11,2.5 5.5,5 0,2.5" fill="#fff"/><path d="M2.5 3.8v2.2c1.8 1.3 4.2 1.3 6 0V3.8" fill="#fff"/></svg><span>Durch das Rangeln und Raufen lernen die Kinder ihren Körper wahrzunehmen. Sie erfahren am eigenen Leib, welche Auswirkungen körperliche Handlungen auf andere haben können</span></li>
            <li><svg width="11" height="8" viewBox="0 0 11 8"><polygon points="5.5,0 11,2.5 5.5,5 0,2.5" fill="#fff"/><path d="M2.5 3.8v2.2c1.8 1.3 4.2 1.3 6 0V3.8" fill="#fff"/></svg><span>Die Kinder erhalten ein realistisches Selbstbild. Sie lernen zu was sie im Stande sind, stoßen aber auch lustvoll an ihre Grenzen</span></li>
          </ul>
        </aside>
      </div>
    </div>
    <div class="wordmark">BODENLERNWERK</div>
    <div class="folio">SEITE 7</div>
  </section>
</main>
</body>
</html>
```